Designing a website for Brightmoor Pest Services PTY LTD

Pest control company looking for someone to build an informative website containing services we offer and an online inquiry form.
Commercial premises - Specialising in - Rodent control, stored product pest control, flying insect control, ant, spider and insect control, Termite inspections and treatments. Termite management systems on a commercial scale.
Facilities we service
Commercial - shopping centres, transport facilities, restaurants, pubs, clubs, bars food manufacturing facilities.
Residential - Houses specialising in - Rodent, Ant, Spider, Cockroach and Termite control. Termite inspections, Pre - purchase inspections, Termite treatments, Termite management systems.
Target Market(s)
Mainly commercial and industrial clients and Residential clients.
Industry/Entity Type
Pest Control
Number of Pages Required
1 page
Look and feel

```html
<!DOCTYPE html>
<html lang="en">
<head>
<meta charset="utf-8">
<title>Brightmoor Pest Services</title>
<link href="https://fonts.googleapis.com/css2?family=League+Spartan:wght@400;600;700;800&family=Lato:ital,wght@0,400;0,700;1,400&display=swap" rel="stylesheet">
<style>
:root{
  --green:#5b9a2a;
  --green-dark:#3f7f1c;
  --blue:#1446a0;
  --blue-light:#2c6fd6;
  --ink:#1c1c1c;
  --text:#333;
  --muted:#666;
  --grey:#e5e6e8;
  --panel:#eef0f2;
  --yellow:#fde53a;
  --footer:#1f2428;
  --white:#fff;
  --head:"League Spartan",sans-serif;
  --body:"Lato",sans-serif;
}
*{margin:0;padding:0;box-sizing:border-box}
html,body{width:1200px;height:3055px;overflow:hidden}
body{position:relative;font-family:var(--body);color:var(--text);background:var(--white)}
.abs{position:absolute}
.photo{position:absolute}
/* header */
.site-header{position:absolute;left:0;top:0;width:1200px;height:137px;background:var(--white)}
.brand{position:absolute;left:35px;top:48px;width:230px;font-family:var(--head);font-weight:800;font-size:21px;line-height:22px;color:var(--ink);display:flex;align-items:center;gap:10px}
.brand-dot{flex:none;width:22px;height:22px;border-radius:50%;background:var(--green)}
.nav{position:absolute;top:58px;left:288px;display:flex;font-family:var(--head);font-size:20px;color:#555}
.nav a{text-decoration:none;color:inherit;margin-right:42px}
.nav a.active{color:var(--green)}
.btn-estimate{position:absolute;left:924px;top:42px;width:247px;height:52px;border-radius:26px;background:var(--green-dark);color:var(--white);font-family:var(--head);font-weight:600;font-size:20px;display:flex;align-items:center;justify-content:center}
/* hero */
.hero{position:absolute;left:0;top:137px;width:1200px;height:728px}
.hero-bg{left:0;top:0;width:1200px;height:728px;background:linear-gradient(100deg,#3f5a26 0%,#7a8c55 22%,#dfe0d8 32%,#c9d07a 55%,#f1e04a 68%,#8aa53a 85%,#3b5a22 100%)}
.hero-the{left:585px;font-family:var(--head);font-weight:700;font-size:26px;color:#8a8f90;transform:rotate(-90deg);transform-origin:left top;top:168px}
.hero-title{left:614px;top:103px;font-family:var(--head);font-weight:800;font-size:72px;line-height:67px;color:var(--green);letter-spacing:-1px;white-space:nowrap}
.hero-call{left:614px;top:327px;width:445px;height:86px;background:var(--green);color:var(--white);padding:12px 54px}
.hero-call small{display:block;font-family:var(--head);font-size:15px}
.hero-call strong{display:block;font-family:var(--head);font-weight:700;font-size:32px;margin-top:4px;white-space:nowrap}
.quote-form{left:113px;top:535px;width:973px;height:145px}
.quote-intro{position:absolute;left:0;top:0;width:265px;height:145px;background:var(--green);color:var(--white);padding:20px 28px}
.quote-intro h2{font-family:var(--head);font-weight:700;font-size:35px;line-height:40px}
.quote-intro p{font-size:13px;margin-top:8px}
.quote-intro::after{content:"";position:absolute;right:-16px;top:56px;border-left:16px solid var(--green);border-top:16px solid transparent;border-bottom:16px solid transparent}
.quote-fields{position:absolute;left:265px;top:0;width:708px;height:145px;background:var(--white)}
.field{position:absolute;width:219px;height:40px;border-bottom:1.5px solid var(--blue);font-family:var(--head);font-weight:700;font-size:12px;color:var(--ink)}
.btn-start{position:absolute;left:537px;top:20px;width:152px;height:106px;background:#222;color:var(--white);font-family:var(--head);font-weight:700;text-align:center;padding-top:24px}
.btn-start b{display:block;font-size:32px;line-height:32px}
.btn-start span{font-size:15px}
/* services */
.services{position:absolute;left:0;top:865px;width:1200px;height:470px}
.card{position:absolute;top:65px;width:256px}
.card .photo{position:relative;width:256px;height:160px}
.card h3{font-family:var(--head);font-weight:700;font-size:19px;color:var(--ink);margin-top:22px;white-space:nowrap;letter-spacing:-0.2px}
.card p{font-size:12.5px;line-height:23px;margin-top:14px;height:96px}
.card .more{font-size:12.5px;color:var(--blue-light);margin-top:10px;display:flex;align-items:center;gap:10px}
.card .more::before{content:"";width:18px;height:1.5px;background:var(--blue-light)}
.guarantee{left:897px;top:0;width:303px;height:470px;background:linear-gradient(160deg,#c9d3de,#eef1f4 40%,#9aa7b5 100%)}
.guarantee .kicker{position:absolute;left:0;width:303px;top:195px;text-align:center;font-family:var(--head);font-weight:700;font-size:16px;color:var(--blue)}
.guarantee h3{position:absolute;left:0;width:303px;top:214px;text-align:center;font-family:var(--head);font-weight:800;font-size:35px;color:var(--blue)}
.guarantee .btn{position:absolute;left:72px;top:271px;width:161px;height:37px;background:var(--blue);color:var(--white);font-family:var(--head);font-weight:700;font-size:15px;display:flex;align-items:center;justify-content:center}
.seal{position:absolute;left:115px;top:370px;width:70px;height:70px;border-radius:50%;background:#1a3f85;border:5px solid #c9a54a}
/* questions */
.faq{position:absolute;left:0;top:1335px;width:600px;height:460px;background:var(--grey)}
.faq-photo{left:345px;top:0;width:255px;height:402px;background:linear-gradient(180deg,#d9dbde,#b8c6d6 60%,#9fb1c8)}
.faq h2{position:absolute;left:47px;top:55px;font-family:var(--head);font-weight:800;font-size:68px;line-height:68px;color:var(--blue);letter-spacing:-1px}
.faq h3{position:absolute;left:47px;top:205px;font-family:var(--head);font-weight:800;font-size:35px;color:var(--blue-light)}
.faq p{position:absolute;left:47px;top:270px;width:350px;font-size:12.5px;line-height:23px}
.faq p a{color:var(--blue-light);text-decoration:none}
.btn-faq{position:absolute;left:237px;top:402px;width:363px;height:58px;background:var(--yellow);font-family:var(--head);font-weight:700;font-size:20px;color:var(--ink);display:flex;align-items:center;padding-left:50px;gap:22px}
.btn-faq::before{content:"";width:48px;height:1.5px;background:var(--ink)}
.info-panel{position:absolute;left:600px;width:600px;height:230px;background:linear-gradient(90deg,#f6f7f8 45%,#e3e5e6)}
.info-panel .photo{left:295px;top:0;width:305px;height:230px}
.info-panel h3{position:absolute;left:46px;top:60px;font-family:var(--head);font-weight:700;font-size:20px;color:var(--blue)}
.info-panel p{position:absolute;left:47px;top:103px;width:270px;font-size:12.5px;line-height:23px}
.info-panel .btn{position:absolute;left:315px;top:183px;width:285px;height:47px;background:var(--blue);color:var(--white);font-family:var(--head);font-weight:700;font-size:15px;display:flex;align-items:center;padding-left:38px;gap:16px}
.info-panel .btn::before{content:"";width:26px;height:1.5px;background:var(--white)}
/* why */
.why{position:absolute;left:0;top:1795px;width:1200px;height:745px}
.why h2{position:absolute;left:47px;top:58px;font-family:var(--head);font-weight:800;font-size:35px;color:var(--ink)}
.why .intro{position:absolute;left:47px;top:118px;width:705px;font-size:12.5px;line-height:23px}
.feature{position:absolute;width:320px}
.feature .icon{position:absolute;left:0;top:0;width:44px;height:44px;border-radius:50%;border:1px solid #cdd5e3;display:flex;align-items:center;justify-content:center}
.feature .icon svg{width:20px;height:20px}
.feature h4{margin-left:65px;font-family:var(--head);font-weight:700;font-size:16px;color:var(--ink);white-space:nowrap}
.feature p{margin-left:65px;margin-top:14px;font-size:12.5px;line-height:23px;width:255px}
.testimonial{left:803px;top:65px;width:350px;height:613px;background:var(--panel)}
.testimonial blockquote{position:absolute;left:45px;top:38px;width:265px;font-style:italic;font-size:16px;line-height:26px;color:var(--blue-light)}
.testimonial .who{position:absolute;left:45px;top:225px;font-size:14px;color:#999;white-space:nowrap}
.testimonial .who b{font-family:var(--head);color:var(--blue);font-size:15px}
.testimonial .photo{left:60px;top:285px;width:290px;height:328px;background:linear-gradient(180deg,#eef0f2,#e2d8d0 40%,#c9b5a6)}
/* footer */
.site-footer{position:absolute;left:0;top:2540px;width:1200px;height:515px}
.footer-brand{position:absolute;left:100px;top:228px;font-family:var(--head);font-weight:700;font-size:34px;line-height:38px;color:var(--white);display:flex;align-items:center;gap:14px}
.footer-brand .dot{width:30px;height:30px;border-radius:50%;border:3px solid var(--white)}
.fcol h4{font-family:var(--head);font-weight:600;font-size:20px;color:var(--white)}
.fcol{position:absolute;top:140px;color:#ddd;font-size:16px}
.contact-item{display:flex;gap:14px;margin-top:24px;line-height:22px}
.contact-item svg{flex:none;width:20px;height:20px;margin-top:1px}
.links a{display:block;color:#ddd;text-decoration:none;line-height:28px}
.social{display:flex;gap:7px;margin-top:70px;margin-left:3px}
.social span{width:34px;height:34px;border-radius:50%;border:2px solid var(--green)}
.footer-bottom{position:absolute;left:0;top:402px;width:1200px;border-top:1px solid #3a4045;height:113px;font-family:var(--head);font-size:15px;color:#ccc}
.footer-bottom .copy{position:absolute;left:100px;top:33px}
.footer-bottom .copy em{font-style:normal;color:var(--green)}
.footer-bottom .legal{position:absolute;right:75px;top:33px}
</style>
</head>
<body>

<header class="site-header">
  <div class="brand"><span class="brand-dot"></span><span>Brightmoor<br>Pest Services</span></div>
  <nav class="nav">
    <a class="active">Home</a><a>About Us</a><a>Services</a><a>Pricing</a><a>Blog</a><a>Contact</a>
  </nav>
  <div class="btn-estimate">Request An Estimate</div>
</header>

<section class="hero">
  <div class="photo hero-bg" role="img" aria-label="Technician in protective suit spraying hedges in sunlit greenery"></div>
  <div class="abs hero-the">THE</div>
  <h1 class="abs hero-title">LIGHTER WAY<br>TO ENJOY<br>PEST CONTROL</h1>
  <div class="abs hero-call"><small>FOR SERVICES &amp; IMMEDIATE ATTENTION 24/7</small><strong>Call Us: (03 5550 1842)</strong></div>
  <form class="abs quote-form">
    <div class="quote-intro"><h2>Get A Free Estimate For</h2><p>Our guys will contact to you</p></div>
    <div class="quote-fields">
      <div class="field" style="left:47px;top:21px">WHAT'S BUGGING YOU?</div>
      <div class="field" style="left:294px;top:21px">YOUR NAME</div>
      <div class="field" style="left:47px;top:79px">YOUR EMAIL</div>
      <div class="field" style="left:294px;top:79px">YOUR PHONE</div>
      <div class="btn-start"><b>GET</b><span>STARTED</span></div>
    </div>
  </form>
</section>

<section class="services">
  <article class="card" style="left:47px">
    <div class="photo" role="img" aria-label="Technician spraying garden hedges" style="background:linear-gradient(180deg,#5f8a3c,#2f5522)"></div>
    <h3>RESIDENTIAL PEST CONTROL</h3>
    <p>Rodent, ant, spider, cockroach and termite control for homes. Termite inspections, pre-purchase inspections and termite management systems.</p>
    <div class="more">What you can expect</div>
  </article>
  <article class="card" style="left:330px">
    <div class="photo" role="img" aria-label="Technician treating kitchen cabinets" style="background:linear-gradient(120deg,#e4dccf,#c9a878 60%,#8b6a48)"></div>
    <h3>COMMERCIAL SERVICES</h3>
    <p>Shopping centres, transport facilities, restaurants, pubs, clubs, bars and food manufacturing. Rodent, stored product and flying insect control.</p>
    <div class="more">Let's work together</div>
  </article>
  <article class="card" style="left:614px">
    <div class="photo" role="img" aria-label="Office interior with tall bookshelves" style="background:linear-gradient(120deg,#5a4a42,#9a8f86 50%,#c7c8c9)"></div>
    <h3>SPECIAL OFFERS</h3>
    <p>Termite inspections and treatments on a commercial scale, with bundled packages for industrial sites and ongoing service agreements.</p>
    <div class="more">See what do we have</div>
  </article>
  <div class="photo guarantee" role="img" aria-label="Smiling couple looking at a guarantee">
    <div class="kicker">MONEY-BACK</div>
    <h3>GUARANTEE</h3>
    <div class="btn">LEARN MORE</div>
    <div class="seal"></div>
  </div>
</section>

<section class="faq">
  <div class="photo faq-photo" role="img" aria-label="Smiling man pointing toward the heading"></div>
  <h2>YOU HAVE<br>QUESTIONS</h2>
  <h3>WE HAVE ANSWERS</h3>
  <p>Don't hesitate to ask us, just <a>leave an email here</a>. Or search hundreds of questions from people just like you for your answer. We're always glad to hear from you.</p>
  <div class="btn-faq">GO TO OUR FAQ AREA</div>
</section>
<section class="info-panel" style="top:1335px">
  <div class="photo" role="img" aria-label="Close-up of a moth" style="background:linear-gradient(90deg,rgba(240,240,240,0),#c9b499 45%,#8a6e4e)"></div>
  <h3>IDENTIFY YOUR PEST</h3>
  <p>Correct indentification of your pest makes controlling it easier and often more effective. Our pest library will help you to find out.</p>
  <div class="btn">DISCOVER OUR LIBRARY</div>
</section>
<section class="info-panel" style="top:1565px">
  <div class="photo" role="img" aria-label="Fumigation worker in respirator outside an apartment building" style="background:linear-gradient(90deg,rgba(240,240,240,0),#c9d3d0 40%,#3a4a40)"></div>
  <h3>WAY TO CONTROL YOUR PEST</h3>
  <p>There are many options for controlling pests, and many of these options are tailored to specific pests or problems.</p>
  <div class="btn">LEARN CONTROL METHOD</div>
</section>

<section class="why">
  <h2>WHY CHOOSE US?</h2>
  <p class="intro">Brightmoor pest control is an industry-leading in Australia. At Brightmoor, we pride ourselves on treating our staff and customers like members of our family, and because of this philosophy, we've become a trusted resource for dependence, quality service in our community. Here is somethings we've committed to bring value to local residents.</p>

  <div class="feature" style="left:47px;top:225px">
    <div class="icon"><svg viewBox="0 0 20 20"><circle cx="10" cy="10" r="9" fill="#1446a0"/><path d="M10 5v5h4" stroke="#fff" stroke-width="1.8" fill="none"/></svg></div>
    <h4>24/7 SERVICE</h4>
    <p>When you find pests in your home, we know that you want them gone as quick as possible, then Brightmoor will offer you full day service.</p>
  </div>
  <div class="feature" style="left:425px;top:225px">
    <div class="icon"><svg viewBox="0 0 20 20"><circle cx="10" cy="8" r="6" fill="#1446a0"/><path d="M6 12l-2 7 6-3 6 3-2-7z" fill="#1446a0"/></svg></div>
    <h4>STATE CERTIFIED TECHNICIANS</h4>
    <p>Our experts are proven that they know what they do by having state-licensed and certification. All our methods and treatments does the work well.</p>
  </div>
  <div class="feature" style="left:47px;top:390px">
    <div class="icon"><svg viewBox="0 0 20 20"><rect x="1" y="5" width="18" height="10" rx="1" fill="#1446a0"/><circle cx="10" cy="10" r="3" fill="#fff"/></svg></div>
    <h4>COST EFFECTIVE SOLUTIONS</h4>
    <p>Brightmoor offers timely, pro-active prevention with minimum impact on your family, home life and budget. That makes us one of the best affordable services.</p>
  </div>
  <div class="feature" style="left:425px;top:390px">
    <div class="icon"><svg viewBox="0 0 20 20"><rect x="2" y="6" width="16" height="11" rx="1" fill="#1446a0"/><rect x="7" y="3" width="6" height="4" fill="none" stroke="#1446a0" stroke-width="1.6"/></svg></div>
    <h4>RESPECTFUL &amp; PROFESSIONAL</h4>
    <p>We treat your home as if it was our own. We keep our appointment and deliver our best everytime we visit your sweet home.</p>
  </div>
  <div class="feature" style="left:47px;top:555px">
    <div class="icon"><svg viewBox="0 0 20 20"><path d="M2 9h4v9H2zM7 9l4-7c2 0 2 2 1 5h5c1 0 2 1 1 2l-2 8H7z" fill="#1446a0"/></svg></div>
    <h4>GUARANTEED RESULTS</h4>
    <p>Every day, more families choose us as their pest control company because of what they get. We also come up with money-back guarantee for our services.</p>
  </div>
  <div class="feature" style="left:425px;top:555px">
    <div class="icon"><svg viewBox="0 0 20 20"><circle cx="10" cy="10" r="8" fill="none" stroke="#1446a0" stroke-width="3"/><circle cx="10" cy="10" r="3" fill="#1446a0"/></svg></div>
    <h4>PRO-ACTIVE CUSTOMER CARE</h4>
    <p>At Brightmoor, we're providing after-sales service which ensures that our customers are satisfied with services of company.</p>
  </div>

  <aside class="abs testimonial">
    <blockquote>"I've found bed bugs 3 days ago. Don't know what to do but call to Brightmoor Pest Control. They came to my house very quickly and provided an effective solution for my issue. Recommended these guys for sure!"</blockquote>
    <div class="who"><b>CLARA WENDT</b> — Kestrel Bay, VIC 3990</div>
    <div class="photo" role="img" aria-label="Portrait of a smiling customer"></div>
  </aside>
</section>

<footer class="site-footer">
  <svg class="abs" style="left:0;top:0" width="1200" height="515" viewBox="0 0 1200 515">
    <path d="M0 105 Q600 -20 1200 105 V515 H0Z" fill="#4a8f24"/>
    <path d="M0 125 Q600 5 1200 125 V515 H0Z" fill="#1f2428"/>
  </svg>
  <div class="footer-brand"><span class="dot"></span>Brightmoor<br>Pest Services</div>
  <div class="fcol" style="left:460px">
    <h4>HAVE ANY QUESTION</h4>
    <div class="contact-item"><svg viewBox="0 0 20 20"><path d="M4 2l4 1 1 4-2 2c1 2 3 4 5 5l2-2 4 1 1 4-2 2C9 19 1 11 2 4z" fill="none" stroke="#5b9a2a" stroke-width="1.4"/></svg>+61 (3) 5550-1842</div>
    <div class="contact-item"><svg viewBox="0 0 20 20"><path d="M10 19s-6-7-6-11a6 6 0 0112 0c0 4-6 11-6 11z" fill="none" stroke="#5b9a2a" stroke-width="1.4"/><circle cx="10" cy="8" r="2" fill="#5b9a2a"/></svg>12 Fernhill Lane, Larkfield Business<br>Park, Kestrel Bay, VIC 3990 Australia</div>
    <div class="contact-item" style="margin-top:40px"><svg viewBox="0 0 20 20"><rect x="2" y="5" width="16" height="11" fill="none" stroke="#5b9a2a" stroke-width="1.4"/><path d="M2 5l8 6 8-6" fill="none" stroke="#5b9a2a" stroke-width="1.4"/></svg>hello@brightmoorpest.example</div>
  </div>
  <div class="fcol links" style="left:803px">
    <h4>INFO</h4>
    <div style="margin-top:20px"><a>Home</a><a>About Us</a><a>Services</a><a>Pricing</a><a>Blog</a><a>Contact Us</a></div>
  </div>
  <div class="fcol" style="left:970px">
    <h4>SOCIAL</h4>
    <div class="social"><span></span><span></span><span></span></div>
  </div>
  <div class="footer-bottom">
    <div class="copy">© 2021 <em>Brightmoor Pest Services.</em> All Rights Reserved.</div>
    <div class="legal">Privacy Policy &nbsp; | &nbsp; Terms of Use</div>
  </div>
</footer>

</body>
</html>
```